New Web Design Project

New Roofing Website homepage mockup

Complete design document here: https://files.plenovark.com/document/d/7kRtWmZpQ2vLxB9nHcYdF4sJgTuEaOiMbNwXzCyVqhr/edit?usp=sharing
Updates

PROJECT IS NOW CLOSED. ANY NEW SUBMISSIONS WILL BE AUTO REJECTED

Number of Pages Required

1 page

Font styles to use
Sans Serif

```html
<!DOCTYPE html>
<html lang="en">
<head>
<meta charset="utf-8">
<title>Steadfast Roofing</title>
<link href="https://fonts.googleapis.com/css2?family=Lato:ital,wght@0,400;0,700;0,900;1,700&display=swap" rel="stylesheet">
<style>
:root{
  --blue:#1f8fd9;
  --blue-dark:#1670b5;
  --ink:#333333;
  --text:#4a4a4a;
  --dark:#2a2a2a;
  --footer:#222326;
  --gray-bg:#f3f3f3;
  --white:#ffffff;
}
*{margin:0;padding:0;box-sizing:border-box}
html,body{width:1200px;height:4574px;overflow:hidden;background:var(--white)}
body{font-family:'Lato',sans-serif;color:var(--text)}
.page{position:relative;width:1200px;height:4574px;overflow:hidden}
.abs{position:absolute}
.center{text-align:center}
.section-title{position:absolute;left:0;width:1200px;text-align:center;font-weight:900;font-size:31px;color:var(--ink);text-transform:uppercase;letter-spacing:.3px}
.lead{position:absolute;left:0;width:1200px;text-align:center;font-size:14px;line-height:28px;color:var(--text)}

/* header */
.topbar{top:14px;right:75px;font-size:15px;color:var(--blue);font-weight:700;display:flex;gap:22px;align-items:center}
.topbar span{display:flex;align-items:center;gap:10px}
.topbar .email{font-size:13px}
.brand{left:75px;top:58px;font-size:22px;font-weight:900;color:var(--blue);letter-spacing:.2px;display:flex;align-items:center;gap:10px}
.brand .mark{width:26px;height:26px;background:var(--blue)}
.nav-rule{left:0;top:57px;width:1200px;height:1px;background:#e4e4e4}
.nav{top:80px;left:310px;display:flex;gap:40px;font-size:13px;font-weight:700;color:var(--ink)}
.nav a{color:inherit;text-decoration:none;padding-bottom:14px}
.nav a.active{color:var(--blue);border-bottom:3px solid var(--blue)}

/* hero */
.hero-photo{top:117px;left:0;width:1200px;height:620px;background:linear-gradient(180deg,#55605a 0%,#8a8f92 35%,#6d716a 65%,#4f5a45 100%)}
.hero-title{top:272px;left:0;width:1200px;text-align:center;color:var(--white);font-weight:900;font-size:64px;line-height:72px;text-shadow:0 2px 6px rgba(0,0,0,.35)}
.btn-blue{background:var(--blue);color:var(--white);font-weight:700;font-size:17px;display:flex;align-items:center;justify-content:center}
.hero-btn{top:444px;left:518px;width:164px;height:40px}
.dots{top:625px;left:538px;display:flex;gap:6px}
.dots i{display:block;width:30px;height:4px;background:rgba(255,255,255,.5)}
.dots i.on{background:var(--blue)}

/* services */
.service-card{width:241px;height:392px;top:958px;background:var(--white);box-shadow:0 2px 8px rgba(0,0,0,.12);clip-path:polygon(0 0,100% 0,100% 100%,0 95%)}
.service-card .photo{height:178px;background:linear-gradient(135deg,#6b7077,#a7a9ab)}
.service-card h3{margin-top:18px;text-align:center;color:var(--blue);font-size:19px;font-weight:700}
.service-card p{margin:8px 24px 0;text-align:center;font-size:14px;line-height:26px;color:var(--text)}

/* what we do */
.wwd-title{top:1456px;left:75px;color:var(--white);font-weight:900;font-size:32px}
.wwd-text{top:1508px;left:75px;width:540px;color:var(--white);font-size:14px;line-height:27.5px}
.btn-outline{border:2px solid var(--white);color:var(--white);font-weight:700;font-size:14px;display:flex;align-items:center;justify-content:center}
.wwd-btn{top:1681px;left:75px;width:148px;height:45px}
.circle-photo{border-radius:50%;border:5px solid var(--blue-dark)}

/* roof types */
.roof-type{top:2049px;width:120px;text-align:center}
.roof-type .disc{width:120px;height:120px;border-radius:50%;border:4px solid var(--blue)}
.roof-type b{display:block;margin-top:16px;color:var(--blue);font-size:19px;font-weight:900}

/* projects */
.project{width:330px;height:247px;background:linear-gradient(180deg,#aeb9c2 0%,#8d9498 55%,#56704a 100%)}
.project-label{color:var(--white);font-weight:900;font-size:27px;display:flex;align-items:center;justify-content:center;text-shadow:0 2px 4px rgba(0,0,0,.4)}

/* estimate */
.estimate-bg{top:3018px;left:0;width:1200px;height:816px}
.est-title{top:3135px;left:0;width:1200px;text-align:center;color:var(--white);font-weight:900;font-size:32px}
.est-sub{top:3204px;left:0;width:1200px;text-align:center;color:var(--white);font-weight:700;font-size:26px}
.step{top:3266px;width:242px;height:38px;border:1px solid rgba(255,255,255,.85);color:var(--white);font-size:13px;font-weight:700;font-style:italic;display:flex;align-items:center;padding-left:14px;gap:22px}
.step:first-of-type{}
.step.first{background:var(--white);color:var(--ink);border-color:var(--ink)}
.est-card{top:3348px;width:242px;height:402px;background:var(--white);text-align:center}
.est-card .photo{height:184px;background:linear-gradient(180deg,#5b5e63,#33363a)}
.est-card .tier{margin-top:22px;font-size:20px;font-weight:700;color:var(--ink)}
.est-card .model{font-size:19px;font-weight:700;color:var(--ink);margin-top:2px}
.est-card .price{font-size:22px;font-weight:900;color:var(--ink);margin-top:8px}
.est-card .info{font-size:14px;font-weight:700;color:var(--ink);text-decoration:underline;margin-top:6px}
.est-card .calc{margin:14px auto 0;width:194px;height:38px;border:2px solid var(--blue);color:var(--blue);font-size:13px;font-weight:900;display:flex;align-items:center;justify-content:center}

/* testimonials */
.quote{top:3952px;left:140px;width:920px;text-align:center;font-size:15.5px;line-height:28px;color:var(--text)}
.quote-name{top:4112px;left:0;width:1200px;text-align:center;color:var(--blue);font-weight:700;font-size:14px}
.qmark{font-family:Georgia,serif;font-size:150px;color:#e2e2e2;font-weight:700;line-height:1}

/* footer */
.footer-bg{top:4198px;left:0;width:1200px;height:376px}
.f-brand{top:4380px;left:75px;font-size:22px;font-weight:900;color:var(--blue);display:flex;align-items:center;gap:10px}
.f-brand .mark{width:26px;height:26px;background:var(--blue)}
.f-copy{top:4452px;left:75px;font-size:12px;line-height:23px;color:var(--white)}
.f-head{color:var(--white);font-weight:700;font-size:17px}
.f-links{color:#d8d8d8;font-size:14px;line-height:32px}
.f-contact{color:#d8d8d8;font-size:13px;line-height:26px}
.f-contact div{display:flex;gap:18px;align-items:flex-start}
.f-contact svg{flex:none;margin-top:7px}
.signup{top:4363px;left:870px;width:256px;height:41px;display:flex}
.signup .field{flex:1;background:var(--white);color:#444;font-size:13px;display:flex;align-items:center;padding-left:12px}
.signup .go{width:82px;background:var(--blue);color:var(--white);font-size:13px;font-weight:700;display:flex;align-items:center;justify-content:center}
.social{top:4487px;left:870px;display:flex;gap:20px}
.social i{display:block;width:22px;height:22px;border-radius:50%;background:#9a9a9a}
</style>
</head>
<body>
<div class="page">

  <!-- header -->
  <div class="abs topbar">
    <span>
      <svg width="14" height="14" viewBox="0 0 24 24" fill="#1f8fd9"><path d="M6.6 10.8a15 15 0 006.6 6.6l2.2-2.2c.3-.3.7-.4 1-.2 1.1.4 2.3.6 3.6.6.6 0 1 .4 1 1V20c0 .6-.4 1-1 1A17 17 0 013 4c0-.6.4-1 1-1h3.5c.6 0 1 .4 1 1 0 1.3.2 2.5.6 3.6.1.3 0 .7-.2 1z"/></svg>
      555-014-2290
    </span>
    <span class="email">
      <svg width="15" height="12" viewBox="0 0 24 18" fill="#1f8fd9"><path d="M0 0h24v2L12 10 0 2z"/><path d="M0 5l12 8 12-8v13H0z"/></svg>
      hello@steadfastroofing.example
    </span>
  </div>
  <div class="abs brand"><span class="mark"></span>STEADFAST ROOFING</div>
  <div class="abs nav-rule"></div>
  <nav class="abs nav">
    <a class="active">HOME</a><a>ABOUT US</a><a>SERVICES</a><a>TYPES OF ROOFS</a><a>RECENT PROJECTS</a><a>CLIENTS</a><a>CONTACT US</a>
  </nav>

  <!-- hero -->
  <div class="abs hero-photo" role="img" aria-label="Aerial photo of a large white house with a new dark shingle roof"></div>
  <svg class="abs" style="top:600px;left:0" width="1200" height="150" viewBox="0 0 1200 150">
    <polygon points="0,57 1200,70 1200,150 0,150" fill="#ffffff"/>
    <polygon points="0,57 1200,68 1200,82 300,137 0,80" fill="#1f8fd9"/>
    <polygon points="0,80 300,137 1200,82 1200,150 0,150" fill="#ffffff"/>
  </svg>
  <h1 class="abs hero-title">BUILT RIGHT,<br>BUILT TO LAST</h1>
  <div class="abs btn-blue hero-btn">READ MORE</div>
  <div class="abs dots"><i class="on"></i><i></i><i></i></div>

  <!-- services -->
  <h2 class="section-title" style="top:810px">OUR SERVICES</h2>
  <p class="lead" style="top:868px">Lorem ipsum dolor sit amet, consectetur adipiscing elit. Nam vehicula pharetra mi, a varius nisl rhoncus volutpat.nunc quis lobortis nisl.<br>Donec sit amet tortor eu tellus ultricies tempus sed quis augue.</p>

  <svg class="abs" style="top:1240px;left:0" width="1200" height="595" viewBox="0 0 1200 595">
    <polygon points="0,38 1200,12 1200,594 0,594" fill="#2a2a2a"/>
    <polygon points="0,56 1200,28 1200,594 0,594" fill="#1f8fd9"/>
  </svg>

  <div class="abs service-card" style="left:75px">
    <div class="photo" role="img" aria-label="Roofer installing shingles on a roof"></div>
    <h3>Roof Installation</h3>
    <p>Lorem ipsum dolor sit amet, consectetur adipiscing elit vehicula pharetra mi, a varius nisl rhoncu..</p>
  </div>
  <div class="abs service-card" style="left:345px">
    <div class="photo" role="img" aria-label="Two roofers repairing a shingle roof"></div>
    <h3>Roof Repair</h3>
    <p>Lorem ipsum dolor sit amet, consectetur adipiscing elit vehicula pharetra mi, a varius nisl rhoncu..</p>
  </div>
  <div class="abs service-card" style="left:615px">
    <div class="photo" role="img" aria-label="Metal gutter and downspout under a red roof" style="background:linear-gradient(180deg,#b84a34 0%,#c9cdd1 45%,#9aa0a5 100%)"></div>
    <h3>Gutters</h3>
    <p>Lorem ipsum dolor sit amet, consectetur adipiscing elit vehicula pharetra mi, a varius nisl rhoncu..</p>
  </div>
  <div class="abs service-card" style="left:885px">
    <div class="photo" role="img" aria-label="Worker installing house siding" style="background:linear-gradient(135deg,#c9a98c,#e6d9c6)"></div>
    <h3>Siding</h3>
    <p>Lorem ipsum dolor sit amet, consectetur adipiscing elit vehicula pharetra mi, a varius nisl rhoncu..</p>
  </div>

  <!-- what we do -->
  <h2 class="abs wwd-title">WHAT WE DO</h2>
  <p class="abs wwd-text">After over a decade of general contracting, we continue to see a repetitive trend by the roof purchase process where homeowners are constantly left confused, nervous, and worried when they need a new roof. As one of the most important features of keeping your home safe, this is unacceptable. Steadfast Roofing was created to break this trend.</p>
  <div class="abs btn-outline wwd-btn">READ MORE</div>
  <div class="abs circle-photo" style="top:1432px;left:793px;width:334px;height:334px;background:linear-gradient(180deg,#9fb3c6 0%,#e8e8e6 45%,#3c4a3a 100%)" role="img" aria-label="Company truck parked in front of a finished house"></div>
  <div class="abs circle-photo" style="top:1443px;left:635px;width:196px;height:196px;background:linear-gradient(180deg,#5f7d48 0%,#8e949a 50%,#41602f 100%)" role="img" aria-label="House with new roof surrounded by trees"></div>

  <!-- types of roofs -->
  <h2 class="section-title" style="top:1893px">TYPES OF ROOFS</h2>
  <p class="lead" style="top:1951px">Lorem ipsum dolor sit amet, consectetur adipiscing elit. Nam vehicula pharetra mi, a varius nisl rhoncus volutpat.nunc quis lobortis nisl.<br>Donec sit amet tortor eu tellus ultricies tempus sed quis augue.</p>
  <div class="abs roof-type" style="left:116px"><div class="disc" role="img" aria-label="Cedar shake roof close-up" style="background:linear-gradient(135deg,#a0714a,#6b4a30)"></div><b>CEDAR</b></div>
  <div class="abs roof-type" style="left:329px"><div class="disc" role="img" aria-label="Metal roof close-up" style="background:linear-gradient(135deg,#c4c8cc,#5a6067)"></div><b>METAL</b></div>
  <div class="abs roof-type" style="left:540px"><div class="disc" role="img" aria-label="Slate roof close-up" style="background:linear-gradient(135deg,#a9bcd0,#4d5a6a)"></div><b>SLATE</b></div>
  <div class="abs roof-type" style="left:753px"><div class="disc" role="img" aria-label="Asphalt shingle roof close-up" style="background:linear-gradient(180deg,#b9c6d3,#3c4148)"></div><b>ASPHALT</b></div>
  <div class="abs roof-type" style="left:966px"><div class="disc" role="img" aria-label="Rubber roof shingles close-up" style="background:linear-gradient(135deg,#9a9ea3,#3c3f44)"></div><b>RUBBER</b></div>

  <!-- recent projects -->
  <div class="abs" style="top:2281px;left:0;width:1200px;height:760px;background:var(--gray-bg)"></div>
  <h2 class="section-title" style="top:2337px">RECENT PROJECTS</h2>
  <div class="abs project project-label" style="top:2409px;left:75px;background:linear-gradient(180deg,#c4cfd8 0%,#7b8690 50%,#3e4144 100%)" role="img" aria-label="Large family home with new roof in Lexington">LEXINGTON</div>
  <div class="abs project" style="top:2409px;left:435px" role="img" aria-label="Colonial house with new grey roof"></div>
  <div class="abs project" style="top:2409px;left:795px" role="img" aria-label="Grey-sided house with new roof"></div>
  <div class="abs project" style="top:2687px;left:75px;background:linear-gradient(135deg,#4a4643,#b7a48f)" role="img" aria-label="Curved roof over arched window"></div>
  <div class="abs project" style="top:2687px;left:435px;background:linear-gradient(180deg,#9aa6b3 0%,#e4e4e4 45%,#3a3c40 100%)" role="img" aria-label="Cupola on a shingle roof"></div>
  <div class="abs project" style="top:2687px;left:795px;background:linear-gradient(180deg,#5b7a44 0%,#98a2a6 50%,#3f5a30 100%)" role="img" aria-label="Green house with new roof among trees"></div>

  <!-- instant estimate -->
  <svg class="abs estimate-bg" viewBox="0 0 1200 816" preserveAspectRatio="none">
    <defs>
      <linearGradient id="estGrad" x1="0" y1="0" x2="0" y2="1">
        <stop offset="0" stop-color="#1f8fd9"/>
        <stop offset=".55" stop-color="#1a78bd"/>
        <stop offset="1" stop-color="#13598f"/>
      </linearGradient>
    </defs>
    <polygon points="0,44 870,0 1200,66 1200,816 0,816" fill="#2a2a2a"/>
    <polygon points="0,60 870,16 1200,84 1200,816 0,816" fill="url(#estGrad)"/>
  </svg>
  <h2 class="abs est-title">INSTANT ESTIMATE</h2>
  <p class="abs est-sub">Choose Your Roof Type?</p>
  <div class="abs step first" style="left:75px"><span>1.</span>PRODUCT SELECTION</div>
  <div class="abs step" style="left:345px"><span>2.</span>ABOUT YOUR ROOF</div>
  <div class="abs step" style="left:615px"><span>3.</span>ROOF CONDITION</div>
  <div class="abs step" style="left:885px"><span>4.</span>GET YOUR COST</div>

  <div class="abs est-card" style="left:75px"><div class="photo" role="img" aria-label="Grey architectural shingles" style="background:linear-gradient(180deg,#6d7075,#43464b)"></div><div class="tier">Good</div><div class="model">Ridgeline Pro HD</div><div class="price">$$$</div><div class="info">View Info</div><div class="calc">CALCULATE YOUR COST</div></div>
  <div class="abs est-card" style="left:345px"><div class="photo" role="img" aria-label="Dark tile roofing" style="background:linear-gradient(180deg,#3a3b3d,#151618)"></div><div class="tier">Better</div><div class="model">Ridgeline Pro HD</div><div class="price">$$$</div><div class="info">View Info</div><div class="calc">CALCULATE YOUR COST</div></div>
  <div class="abs est-card" style="left:615px"><div class="photo" role="img" aria-label="Brown shingles" style="background:linear-gradient(180deg,#5a4638,#2e241e)"></div><div class="tier">Best</div><div class="model">Ridgeline Pro HD</div><div class="price">$$$</div><div class="info">View Info</div><div class="calc">CALCULATE YOUR COST</div></div>
  <div class="abs est-card" style="left:885px"><div class="photo" role="img" aria-label="Weathered brown shingles" style="background:linear-gradient(180deg,#7a6f68,#4a403b)"></div><div class="tier">Good</div><div class="model">Ridgeline Pro HD</div><div class="price">$$$</div><div class="info">View Info</div><div class="calc">CALCULATE YOUR COST</div></div>

  <!-- testimonials -->
  <h2 class="section-title" style="top:3886px">TESTIMONIALS</h2>
  <div class="abs qmark" style="top:3900px;left:72px">&#8220;</div>
  <div class="abs qmark" style="top:4098px;left:1064px">&#8221;</div>
  <p class="abs quote">We needed to put a new roof on our house, as well as repair a sagging porch roof. Shingles had been flying off and we had had several leaks. Evan provided a very reasonable estimate - well below some of the other HomeCrest companies. The work was done very promptly and professionally. A couple of issues that arose were settled to our satisfaction and Evan took full ownership of the situation. It was very clear that customer satisfaction is a priority for this company. I would definitely recommend and hire again."</p>
  <div class="abs quote-name">DAN WHITFIELD</div>
  <svg class="abs" style="top:4036px;left:62px" width="16" height="26" viewBox="0 0 16 26"><polyline points="13,2 3,13 13,24" fill="none" stroke="#555" stroke-width="3"/></svg>
  <svg class="abs" style="top:4036px;left:1110px" width="16" height="26" viewBox="0 0 16 26"><polyline points="3,2 13,13 3,24" fill="none" stroke="#555" stroke-width="3"/></svg>

  <!-- footer -->
  <svg class="abs footer-bg" viewBox="0 0 1200 376" preserveAspectRatio="none">
    <polygon points="0,62 320,0 1200,40 1200,376 0,376" fill="#1f8fd9"/>
    <polygon points="0,76 320,14 1200,52 1200,376 0,376" fill="#222326"/>
  </svg>
  <div class="abs f-brand"><span class="mark"></span>STEADFAST ROOFING</div>
  <div class="abs f-copy">Copyright © 2020. Company Name.<br>All Right Reserved</div>

  <div class="abs f-head" style="top:4322px;left:343px">SITE MAP</div>
  <div class="abs f-links" style="top:4350px;left:343px">Home<br>About Us<br>Services<br>Types Of Roofs</div>
  <div class="abs f-links" style="top:4350px;left:474px">Recent Projects<br>Clients<br>Contact Us</div>

  <div class="abs f-head" style="top:4322px;left:632px">CONTACT INFO</div>
  <div class="abs f-contact" style="top:4352px;left:632px;width:220px">
    <div><svg width="10" height="13" viewBox="0 0 10 14" fill="#d8d8d8"><path d="M5 0a5 5 0 00-5 5c0 4 5 9 5 9s5-5 5-9a5 5 0 00-5-5zm0 7a2 2 0 110-4 2 2 0 010 4z"/></svg><span>48 Alder Ln. Brookfield<br>MA 01506</span></div>
    <div style="margin-top:6px"><svg width="11" height="11" viewBox="0 0 24 24" fill="#d8d8d8"><path d="M6.6 10.8a15 15 0 006.6 6.6l2.2-2.2c.3-.3.7-.4 1-.2 1.1.4 2.3.6 3.6.6.6 0 1 .4 1 1V20c0 .6-.4 1-1 1A17 17 0 013 4c0-.6.4-1 1-1h3.5c.6 0 1 .4 1 1 0 1.3.2 2.5.6 3.6.1.3 0 .7-.2 1z"/></svg><span>555-014-2291</span></div>
    <div style="margin-top:6px"><svg width="12" height="10" viewBox="0 0 24 18" fill="#d8d8d8"><path d="M0 0h24v2L12 10 0 2z"/><path d="M0 5l12 8 12-8v13H0z"/></svg><span>hello@steadfastroofing.example</span></div>
  </div>

  <div class="abs f-head" style="top:4322px;left:870px">EMAIL SIGN UP</div>
  <div class="abs signup"><div class="field">Enter Email</div><div class="go">SIGN UP</div></div>
  <div class="abs f-head" style="top:4444px;left:870px">FOLLOW US</div>
  <div class="abs social"><i></i><i></i><i></i><i></i><i></i></div>

</div>
</body>
</html>
```